Bill board design For Marlowe’s Construction

Billboard Design Request
Please design the billboard to match the branding, colors, and overall feel of our website: Marlowe's Construction Website
MARLOWE’S CONSTRUCTION
CONCRETE BUILT FOR GENERATIONS
⭐ 5-Star Rated on Zorvix
Please Include:
* All three attached project photos
* Company logo(s)
* Phone Number: 555-214-7630
* Website: MarlowesConstruction.example
* Zorvix logo with 5-star rating graphic
* Chatterly logo
* Pixtoria logo
Service Area:
Kalamazoo • Battle Creek • Coldwater • Grand Rapids
Please arrange the photos and layout in whatever way creates the strongest visual impact and readability from the road. The company name, headline, phone number, and website should be highly visible at highway speeds.
The overall appearance should be clean, professional, premium, and consistent with our website branding while highlighting our reputation, craftsmanship, and quality concrete work.
People Driving By
Concrete Construction

```html
<!DOCTYPE html>
<html lang="en">
<head>
<meta charset="utf-8">
<title>Marlowe’s Construction Billboard</title>
<link href="https://fonts.googleapis.com/css2?family=Montserrat:wght@700&family=Roboto:wght@700&display=swap" rel="stylesheet">
<style>
  :root {
    --brand-blue: #1295e6;
    --brand-blue-light: #3aa6ea;
    --band-grey: #6d6e70;
    --paper: #ffffff;
    --stage: #e9eef2;
    --badge-ink: #2a2a2a;
    --badge-gold-dark: #b8912c;
  }
  html, body {
    margin: 0;
    width: 1200px;
    height: 800px;
    overflow: hidden;
    background: var(--stage);
  }
  .billboard {
    position: absolute;
    left: 0;
    top: 45px;
    width: 1200px;
    height: 710px;
    display: block;
  }
  .phone-number {
    font-family: "Roboto", Arial, sans-serif;
    font-weight: 700;
    font-size: 88px;
    fill: var(--paper);
  }
  .web-address {
    font-family: "Roboto", Arial, sans-serif;
    font-weight: 700;
    font-size: 42px;
    fill: var(--paper);
  }
  .brand-name {
    font-family: "Montserrat", Arial, sans-serif;
    font-weight: 700;
  }
  .brand-name--main { font-size: 70px; fill: var(--brand-blue); }
  .brand-name--sub { font-size: 27px; letter-spacing: 8px; fill: var(--band-grey); }
  .badge-text {
    font-family: "Roboto", Arial, sans-serif;
    font-weight: 700;
    fill: var(--badge-ink);
  }
  .badge-text--line { font-size: 16px; }
  .badge-text--name { font-size: 22px; }
  .social-name {
    font-family: "Roboto", Arial, sans-serif;
    font-weight: 700;
    font-size: 28px;
    fill: var(--paper);
  }
</style>
</head>
<body>
<svg class="billboard" viewBox="0 0 1200 710" xmlns="http://www.w3.org/2000/svg" aria-label="Marlowe’s Construction billboard">
  <defs>
    <linearGradient id="scene-fade" x1="0" y1="0" x2="1" y2="1">
      <stop offset="0" stop-color="#4aa9e6"/>
      <stop offset="1" stop-color="#2f9be3"/>
    </linearGradient>
    <linearGradient id="walkway-tones" x1="0" y1="0" x2="0" y2="1">
      <stop offset="0" stop-color="#6d5a48"/>
      <stop offset="1" stop-color="#b7704a"/>
    </linearGradient>
    <linearGradient id="crew-tones" x1="0" y1="0" x2="1" y2="1">
      <stop offset="0" stop-color="#7e8a5a"/>
      <stop offset="1" stop-color="#5a4a3c"/>
    </linearGradient>
    <linearGradient id="driveway-tones" x1="0" y1="0" x2="0" y2="1">
      <stop offset="0" stop-color="#8a7f86"/>
      <stop offset="1" stop-color="#d9cfc4"/>
    </linearGradient>
    <radialGradient id="badge-gold" cx="0.4" cy="0.35" r="0.7">
      <stop offset="0" stop-color="#f2d77a"/>
      <stop offset="1" stop-color="var(--badge-gold-dark)"/>
    </radialGradient>
  </defs>

  <rect class="field" x="0" y="0" width="1200" height="710" fill="var(--brand-blue)"/>

  <rect class="backdrop-scene" x="870" y="0" width="330" height="710" fill="url(#scene-fade)" opacity="0.85"
        role="img" aria-label="Faded photo of a finished home with trees"/>

  <polygon class="web-band" points="0,132 700,132 645,186 0,186" fill="var(--band-grey)"/>

  <g class="phone-line">
    <circle cx="54" cy="71" r="35" fill="var(--paper)"/>
    <path d="M42 52 q-6 4 -4 14 q6 22 26 30 q9 3 13 -3 l3 -5 -11 -8 -5 5 q-12 -5 -16 -17 l5 -5 -7 -12 z" fill="var(--brand-blue)"/>
    <text class="phone-number" x="104" y="104">555-214-7630</text>
  </g>

  <text class="web-address" x="21" y="173">MarlowesConstruction.example</text>

  <polygon class="brand-panel" points="0,210 664,210 805,355 645,521 0,521" fill="var(--paper)"/>
  <g class="brand-wordmark">
    <text class="brand-name brand-name--main" x="330" y="378" text-anchor="middle">MARLOWE’S</text>
    <text class="brand-name brand-name--sub" x="330" y="422" text-anchor="middle">CONSTRUCTION L.L.C</text>
  </g>

  <g class="project-frames">
    <polygon points="823,22 986,186 823,350 660,186" fill="var(--paper)"/>
    <polygon points="823,48 961,186 823,324 685,186" fill="url(#walkway-tones)"
             role="img" aria-label="Photo of a stamped concrete walkway leading to a house"/>

    <polygon points="990,187 1154,351 990,515 826,351" fill="var(--paper)"/>
    <polygon points="990,213 1128,351 990,489 852,351" fill="url(#crew-tones)"
             role="img" aria-label="Photo of a crew member finishing concrete in a yard"/>

    <polygon points="823,354 986,518 823,682 660,518" fill="var(--paper)"/>
    <polygon points="823,380 961,518 823,656 685,518" fill="url(#driveway-tones)"
             role="img" aria-label="Photo of a new concrete driveway in front of a garage"/>
  </g>

  <g class="rating-badge">
    <circle cx="100" cy="618" r="73" fill="var(--paper)"/>
    <circle cx="100" cy="618" r="63" fill="url(#badge-gold)"/>
    <text class="badge-text badge-text--line" x="100" y="603" text-anchor="middle">5-STAR</text>
    <text class="badge-text badge-text--line" x="100" y="620" text-anchor="middle">RATING</text>
    <text class="badge-text badge-text--name" x="100" y="643" text-anchor="middle">Zorvix</text>
  </g>

  <g class="social-links">
    <rect x="200" y="600" width="34" height="34" rx="8" fill="none" stroke="var(--paper)" stroke-width="5"/>
    <text class="social-name" x="246" y="628">Pixtoria</text>
    <rect x="380" y="600" width="34" height="34" rx="8" fill="none" stroke="var(--paper)" stroke-width="5"/>
    <text class="social-name" x="426" y="628">Chatterly</text>
  </g>
</svg>
</body>
</html>
```